Business Card Design Project

Looking for a business card that our customers will remember. We are a high end Travel Agency.
Need a re-memorable classy business card.
Both sides full color.
Must have the following details.
Voyage Harbor Logo (see attached)
4B Wattle Lane
Penhurst Sydney NSW 2241
Phone: 02 9471 3652
Fax: 02 9563 4417
sales@voyageharbor-example.com.au
Consultant Name
Anything else you think we need

```html
<!DOCTYPE html>
<html lang="en">
<head>
<meta charset="utf-8">
<title>Voyage Harbor Business Card</title>
<link href="https://fonts.googleapis.com/css2?family=Questrial&display=swap" rel="stylesheet">
<style>
  :root {
    --backdrop: #4a4a4a;
    --card: #ffffff;
    --navy: #1f4e79;
    --ink: #1a1a1a;
    --gold: #f5c518;
    --ghost: #e8e8ea;
    --rule: #8a8a8a;
  }
  * { margin: 0; padding: 0; box-sizing: border-box; }
  html, body { width: 1200px; height: 900px; overflow: hidden; }
  body {
    background: var(--backdrop);
    font-family: "Questrial", "Century Gothic", sans-serif;
    color: var(--ink);
    position: relative;
  }
  .card {
    position: absolute;
    top: 300px;
    width: 525px;
    height: 300px;
    background: var(--card);
    border-radius: 18px;
    overflow: hidden;
  }
  .card--front { left: 58px; }
  .card--back { left: 617px; }

  .brand {
    position: absolute;
    display: flex;
    align-items: center;
    gap: 10px;
    color: var(--navy);
    white-space: nowrap;
  }
  .brand__dot {
    border-radius: 50%;
    background: var(--gold);
    flex: none;
  }
  .card--front .brand { left: 39px; top: 110px; font-size: 38px; }
  .card--front .brand__dot { width: 22px; height: 22px; }
  .card--back .brand { left: 51px; top: 58px; font-size: 22px; }
  .card--back .brand__dot { width: 13px; height: 13px; }

  .web-line {
    position: absolute;
    left: 52px;
    top: 190px;
    font-size: 14px;
  }
  .rule {
    position: absolute;
    left: 0;
    border-top: 1px dotted var(--rule);
  }
  .card--front .rule { top: 211px; width: 224px; }
  .card--back .rule { top: 175px; width: 231px; }

  .ghost-word {
    position: absolute;
    left: 2px;
    bottom: -22px;
    font-size: 80px;
    line-height: 1;
    color: var(--ghost);
    letter-spacing: -2px;
    white-space: nowrap;
  }

  .consultant {
    position: absolute;
    left: 51px;
    top: 148px;
    font-size: 24px;
    color: var(--ink);
  }
  .consultant__first { color: var(--navy); font-style: italic; }

  .contact-list {
    position: absolute;
    left: 0;
    top: 181px;
    list-style: none;
  }
  .contact-list li {
    display: flex;
    align-items: center;
    height: 15px;
  }
  .tag {
    display: inline-block;
    width: 47px;
    height: 11px;
    background: var(--gold);
    font-size: 8px;
    line-height: 11px;
    text-align: right;
    padding-right: 4px;
    margin-right: 4px;
  }
  .contact-list .value { font-size: 14px; }

  .address {
    position: absolute;
    right: 51px;
    top: 180px;
    text-align: right;
    font-size: 14px;
    line-height: 15px;
  }
  .address-tag {
    position: absolute;
    right: 0;
    top: 182px;
    text-align: left;
    padding-left: 4px;
    margin: 0;
  }
</style>
</head>
<body>
  <section class="card card--front" aria-label="Card front">
    <div class="brand"><span class="brand__name">Voyage Harbor</span><span class="brand__dot"></span></div>
    <p class="web-line">www.voyageharbor-example.com.au</p>
    <div class="rule"></div>
    <p class="ghost-word" aria-hidden="true">voyageharbor</p>
  </section>

  <section class="card card--back" aria-label="Card back">
    <div class="brand"><span class="brand__name">Voyage Harbor</span><span class="brand__dot"></span></div>
    <p class="consultant"><span class="consultant__first">Dorian</span>Whitcombe</p>
    <div class="rule"></div>
    <ul class="contact-list">
      <li><span class="tag">phone</span><span class="value">02 9471 3652</span></li>
      <li><span class="tag">fax</span><span class="value">02 9563 4417</span></li>
      <li><span class="tag">email</span><span class="value">sales@voyageharbor-example.com.au</span></li>
      <li><span class="tag">web</span><span class="value">www.voyageharbor-example.com.au</span></li>
    </ul>
    <p class="address">4B Wattle Lane<br>Penhurst Sydney NSW 2241</p>
    <span class="tag address-tag">address</span>
    <p class="ghost-word" aria-hidden="true">voyageharbor</p>
  </section>
</body>
</html>
```